CodeVarnaly.com Redesign

Please read the notes and see the site-map attached.
Updates

We are looking for something highly creative. Please provide your best work. Best of luck and thank you very much for your hard work!

Reason: I am seeing good designs but I am not seeing great designs. I really need a design that is unique and is going to wow me. No one is required to stick to the existing color schemes etc. You are free to use other colors etc. I am seeing a lot of the same colors that are used on the site now.

Target Market(s)

Business and entrepreneurs mainly. People looking to build applications, software or launch web or mobile tech products.

Colors

Designer to choose colors to be used in the design.

Requirements
Must have
• See my attached html file.
Nice to have
Should not have
• No sure

```html
<!DOCTYPE html>
<html lang="en">
<head>
<meta charset="utf-8">
<title>codevarnaly — Home</title>
<link href="https://fonts.googleapis.com/css2?family=Roboto:wght@300;400;500&family=Open+Sans:ital,wght@0,400;0,600;1,400;1,600&display=swap" rel="stylesheet">
<style>
:root{
  --green:#7bbf3e;
  --green-light:#8dcc4a;
  --green-dark:#5ea22d;
  --teal:#1f4c5f;
  --dark:#1d1d1d;
  --text:#444;
  --muted:#8a8a8a;
  --card:#eeeeee;
  --footer:#e9e9e9;
  --white:#fff;
}
*{box-sizing:border-box;margin:0;padding:0}
html,body{width:787px;height:1200px;overflow:hidden;background:var(--white)}
body{position:relative;font-family:"Open Sans",Arial,sans-serif;color:var(--text)}
.abs{position:absolute}

/* header */
.brand{left:82px;top:24px;height:34px;display:flex;align-items:center;gap:10px}
.brand-mark{width:34px;height:34px;border-radius:50%;background:var(--teal)}
.brand-name{font:400 27px/34px "Roboto",sans-serif;color:var(--green)}
.quote-btn{left:598px;top:30px;width:108px;height:27px;background:var(--teal);color:var(--white);font:400 14px/27px "Roboto",sans-serif;text-align:center;border-radius:2px}

/* nav */
.nav{left:0;top:92px;width:787px;height:32px;background:var(--green)}
.nav-item{position:absolute;top:0;height:32px;font:400 11.5px/32px "Roboto",sans-serif;color:#24414d;text-align:center}
.nav-item.active{background:var(--teal);color:var(--white);font-weight:500}
.nav-sep{position:absolute;top:0;width:1px;height:32px;background:rgba(0,0,0,.12)}
.nav-caret{left:107px;top:88px;width:0;height:0;border-left:5px solid transparent;border-right:5px solid transparent;border-bottom:4px solid var(--teal)}

/* hero */
.hero{left:0;top:124px;width:787px;height:300px;background:radial-gradient(ellipse at 40% 40%,#6a5a4a 0%,#3a332e 45%,#1f1f22 100%)}
.hero-device{left:84px;top:146px;width:180px;height:278px;border-radius:8px;background:linear-gradient(160deg,#f3f3f3 0%,#cfe3ee 50%,#d9b59a 100%)}
.hero-title{left:360px;top:160px;font:300 37px/44px "Roboto",sans-serif;color:var(--green-light)}
.hero-sub{left:362px;top:221px;font:400 14.5px/18px "Roboto",sans-serif;color:var(--white)}
.hero-copy{left:362px;top:257px;font:400 9.5px/17.6px "Roboto",sans-serif;color:#d8d8d8;white-space:nowrap}
.hero-btn{left:526px;top:317px;width:132px;height:33px;background:var(--green);border:2px solid #5a9a2a;color:#132a12;font:500 15px/29px "Roboto",sans-serif;text-align:center;box-shadow:0 0 10px rgba(0,0,0,.5)}

/* welcome */
.welcome-title{left:82px;top:440px;font:400 19px/26px "Roboto",sans-serif;color:var(--green)}
.welcome-title span{color:var(--teal)}
.welcome-copy{left:82px;top:469px;width:425px;font-size:8.8px;line-height:17.6px;text-align:justify;color:#4a4a4a}
.video{left:532px;top:446px;width:174px;height:108px;background:linear-gradient(135deg,#2b3a44,#5a6670 60%,#8a8f92)}
.play{left:601px;top:483px;width:34px;height:34px}
.chat{left:643px;top:541px;width:138px;height:28px;background:var(--green)}
.chat-icon{left:643px;top:519px;width:43px;height:50px;background:var(--green)}
.chat-label{left:694px;top:541px;height:28px;font:400 11.5px/28px "Roboto",sans-serif;color:var(--white)}
.chat-plus{left:753px;top:546px;width:17px;height:17px;background:var(--green-dark);color:var(--white);font:700 13px/17px Arial,sans-serif;text-align:center}

/* case studies */
.cases-title{left:83px;top:567px;font:400 19px/26px "Roboto",sans-serif;color:var(--teal)}
.cases-title span{color:var(--green)}
.card{top:602px;width:193px;height:213px;background:var(--card)}
.card.featured{background:var(--teal);padding:11px}
.featured-head{font:400 12.8px/18.6px "Roboto",sans-serif;color:var(--green-light)}
.featured-cat{margin-top:7px;font:600 10px/14px "Open Sans",sans-serif;color:var(--white)}
.featured-copy{margin-top:8px;font-size:8px;line-height:15.2px;color:var(--white);text-align:justify}
.featured-link{margin-top:8px;text-align:right;font:italic 400 9.5px/14px "Open Sans",sans-serif;color:var(--green-light)}
.card-img{width:193px;height:112px}
.card-body{padding:15px 11px 0}
.card-cat{font:600 9.8px/14px "Open Sans",sans-serif;color:#444}
.card-title{margin-top:8px;font:400 13px/17px "Roboto",sans-serif;color:var(--teal)}
.card-copy{margin-top:8px;font-size:8.5px;line-height:13.6px;color:var(--muted);white-space:nowrap}

/* testimonials */
.testi{left:0;top:839px;width:787px;height:169px;background:linear-gradient(90deg,#2a2622,#3b342e 50%,#26221f)}
.testi-title{left:82px;top:852px;font:400 19px/26px "Roboto",sans-serif;color:var(--green)}
.testi-photo{left:82px;top:896px;width:82px;height:75px;background:linear-gradient(135deg,#e8c99a,#8aa9c8)}
.quote-mark{font:700 42px/42px Georgia,serif;color:#6a6a6a}
.testi-copy{left:212px;top:900px;font-size:8.6px;line-height:17.6px;color:#cfcfcf;white-space:nowrap}
.testi-rule{left:588px;top:896px;width:1px;height:76px;background:#7a7a7a}
.testi-name{left:604px;top:918px;font:400 9.5px/14px "Open Sans",sans-serif;color:var(--green-light)}
.testi-role{left:604px;top:936px;font:italic 400 8.8px/13px "Open Sans",sans-serif;color:#e6e6e6}

/* footer */
.footer{left:0;top:1008px;width:787px;height:154px;background:var(--footer)}
.foot-head{font:400 11.5px/16px "Roboto",sans-serif;color:var(--teal)}
.foot-rule{height:3px;background:#cfcfcf}
.foot-links{left:82px;top:1050px;font-size:8px;line-height:16.2px;color:#444;list-style:none}
.contact{left:282px;top:1052px;font-size:8px;color:#444}
.contact dt{font:italic 400 9.5px/13px Georgia,serif;color:var(--teal)}
.contact dd{line-height:11px;margin-bottom:6px}
.field{background:var(--white);border:1px solid #cfcfcf;font:italic 400 8px/10px "Open Sans",sans-serif;color:#aaa;padding:5px 7px}
.submit{left:649px;top:1132px;width:57px;height:20px;background:var(--green);color:#132a12;font:500 11px/20px "Roboto",sans-serif;text-align:center}

/* bottom bar */
.bar{left:0;top:1162px;width:787px;height:38px;background:var(--dark)}
.copyright{left:82px;top:1175px;font-size:8px;line-height:12px;color:#aaa}
.social{top:1170px;width:23px;height:23px;border-radius:50%;border:1px solid #777}
.social.primary{background:#3b5ea8;border-color:#3b5ea8}
</style>
</head>
<body>

<header>
  <div class="abs brand"><span class="brand-mark"></span><span class="brand-name">codevarnaly</span></div>
  <a class="abs quote-btn">Get a Quote</a>
</header>

<div class="abs nav-caret"></div>
<nav class="abs nav">
  <span class="nav-item active" style="left:82px;width:60px">Home</span>
  <span class="nav-sep" style="left:142px"></span>
  <span class="nav-item" style="left:142px;width:95px">Who We Are</span>
  <span class="nav-sep" style="left:237px"></span>
  <span class="nav-item" style="left:237px;width:92px">What We Do</span>
  <span class="nav-sep" style="left:329px"></span>
  <span class="nav-item" style="left:329px;width:75px">Services</span>
  <span class="nav-sep" style="left:404px"></span>
  <span class="nav-item" style="left:404px;width:154px">Our Work / Case Studies</span>
  <span class="nav-sep" style="left:558px"></span>
  <span class="nav-item" style="left:558px;width:54px">Blog</span>
  <span class="nav-sep" style="left:612px"></span>
  <span class="nav-item" style="left:612px;width:80px">Reach Us</span>
</nav>

<section>
  <div class="abs hero" role="img" aria-label="Blurred office background"></div>
  <div class="abs hero-device" role="img" aria-label="Hand holding a tablet showing a website"></div>
  <h1 class="abs hero-title">Lorem ipsum dolor</h1>
  <p class="abs hero-sub">Consectetur adipiscing adipiscing leo pretium</p>
  <p class="abs hero-copy">Etiam pulvinar ligula tortor, et dsim magna lobortis ut Fusce leo mauris,<br>Coulputate quis nisi sit ametluctus mi.</p>
  <a class="abs hero-btn">Case Studies</a>
</section>

<section>
  <h2 class="abs welcome-title">Welcome to <span>codevarnaly</span></h2>
  <p class="abs welcome-copy">Lorem ipsum dolor sit amet, consectetur adipiscing elit. Praesent adipiscing leo a venenatis pretium. Etiam pulvinar ligula tortor, et dignissim magna lobortis ut. Fusce leo mauris, vulputate quis nisi sit amet, hendrerit luctus mi. Sed auctor neque metus, in dictum neque semper scelerisque. Etiam lacinia sem sit amet mauris euismod rhoncus. Morbi sed dui id ante eleifend fringilla id id est. Nam quis pulvinar tortor, quis ultricies ligula.</p>
  <div class="abs video" role="img" aria-label="Video still of two colleagues at a computer"></div>
  <svg class="abs play" viewBox="0 0 34 34"><circle cx="17" cy="17" r="15.5" fill="rgba(0,0,0,.3)" stroke="#7bbf3e" stroke-width="2"/><path d="M13 10 L24 17 L13 24Z" fill="#7bbf3e"/></svg>
  <div class="abs chat"></div>
  <div class="abs chat-icon"></div>
  <span class="abs chat-label">Live chat</span>
  <span class="abs chat-plus">+</span>
</section>

<section>
  <h2 class="abs cases-title">Case <span>Studies</span></h2>
  <article class="abs card featured" style="left:82px">
    <p class="featured-head">Lorem ipsum dolor sit amet Consectetur adipiscing elit. Praesent adipiscing ipsumdo Consectetur adipiscing elit.</p>
    <p class="featured-cat">Project Category Name</p>
    <p class="featured-copy">Lorem ipsum dolor sit amet, consectetur adipiscing elit. Praesent adipiscing leo a venenatis pretium. Etiam pulvinar ligula tortor, et dignis magna lobortis ut.</p>
    <p class="featured-link">View case study »</p>
  </article>
  <article class="abs card" style="left:298px">
    <div class="card-img" role="img" aria-label="Person holding a pink smartphone" style="background:linear-gradient(135deg,#2a6a8a,#b8d35a 55%,#e4c060)"></div>
    <div class="card-body">
      <p class="card-cat">Project Category Name</p>
      <p class="card-title">Lorem ipsum dolor sit amet</p>
      <p class="card-copy">Consectetur adipiscing elit. adipiscing<br>leo a venenatis pretium.</p>
    </div>
  </article>
  <article class="abs card" style="left:513px">
    <div class="card-img" role="img" aria-label="Smartphone with earphones on a keyboard" style="background:linear-gradient(135deg,#dcdcdc,#8a8a8a 55%,#2e2e2e)"></div>
    <div class="card-body">
      <p class="card-cat">Project Category Name</p>
      <p class="card-title">Lorem ipsum dolor sit amet</p>
      <p class="card-copy">Consectetur adipiscing elit. adipiscing<br>leo a venenatis pretium.</p>
    </div>
  </article>
</section>

<section>
  <div class="abs testi" role="img" aria-label="Blurred crowd background"></div>
  <h2 class="abs testi-title">Testimonials</h2>
  <div class="abs testi-photo" role="img" aria-label="Portrait of a client on the phone"></div>
  <span class="abs quote-mark" style="left:184px;top:890px">“</span>
  <p class="abs testi-copy">Lorem ipsum dolor sit amet, consectr adipiscing elit. Cras porta arcu nec orcaccumsan t<br>empus. Etiam rit gravida ligula sed condimentum. Ndio erat, lobortis sit amet commodo<br>lorem ispumac, iaculis sit amet nibh. Aenean dapibus erat auod mollis ut ac purus.<br>Etiam rit gravida ligula sed condi</p>
  <span class="abs quote-mark" style="left:373px;top:950px">”</span>
  <div class="abs testi-rule"></div>
  <p class="abs testi-name">Lorem ispum dolor</p>
  <p class="abs testi-role">Senior Director</p>
</section>

<footer>
  <div class="abs footer"></div>
  <h3 class="abs foot-head" style="left:82px;top:1022px">Information</h3>
  <div class="abs foot-rule" style="left:82px;top:1041px;width:108px"></div>
  <ul class="abs foot-links">
    <li>Home</li><li>Who We Are</li><li>What We Do</li><li>Services</li><li>Our Work / Case Studies</li><li>Reach Us</li>
  </ul>
  <h3 class="abs foot-head" style="left:282px;top:1022px">Get a Quote</h3>
  <div class="abs foot-rule" style="left:282px;top:1041px;width:424px"></div>
  <dl class="abs contact">
    <dt>Address:</dt><dd>4417 Harbor Lane, Suite 12<br>Westbrook 560210</dd>
    <dt>Telephone:</dt><dd>+91 555 014 2278</dd>
    <dt>E-mail:</dt><dd>info@codevarnaly.com</dd>
  </dl>
  <div class="abs field" style="left:419px;top:1054px;width:137px;height:20px">Name</div>
  <div class="abs field" style="left:568px;top:1054px;width:138px;height:20px">Email</div>
  <div class="abs field" style="left:419px;top:1083px;width:287px;height:39px">Message</div>
  <a class="abs submit">Submit</a>

  <div class="abs bar"></div>
  <p class="abs copyright">© Copyright 2014 code varnaly. All rights reserved.</p>
  <span class="abs social primary" style="left:566px" aria-label="Social link"></span>
  <span class="abs social" style="left:595px" aria-label="Social link"></span>
  <span class="abs social" style="left:625px" aria-label="Social link"></span>
  <span class="abs social" style="left:654px" aria-label="Social link"></span>
  <span class="abs social" style="left:683px" aria-label="Social link"></span>
</footer>

</body>
</html>
```